Chocolate company needing sticker for products

I have a small chocolate company Brook Lane Sweets in Austin Texas. I make all vegan, gluten free, organic, faire trade chocolate that tastes amazing! It is allergy friendly approvable by all ages. I want to have a great sticker that i can put on our boxes and bags. I am using a lot of natural craft color and brown. I am open to color options possibly for different flavors. I want the packaging to reflect the basis of my company. It is all handmade by me but i don't want it to have to much of a crafty look to it. I have attached the logo designs I have. it the sticker can have som of the bullet points about the company that would be great. But it needs to say Locally Made in Austin Texas. it also has to have the company address.
417 West Harlow Pine Rd #238 Austin Tx 78719. These things are required by the state for food regulations. I want something that looks great and I can be really proud to put on my product! Thanks so much for all of your help in advance. Dee

I also need some other information added to the sticker. Website which is brooklanesweetsqvz.com 

Phone number 512.555.0187. Instagram brooklanesweets. Thanks for your hard work! 

Industry/Entity Type

Chocolate Company

Requirements
Must have
• The logo is added at the bottom as well as designs I like I want to have a professional look but it to be approvable by all consumers. I will gig feed back as i see what designs come through. This will probably fold out into a multi design project so i will be looking for assistance on other areas of this as well. Thanks

```html
<!DOCTYPE html>
<html lang="en">
<head>
<meta charset="utf-8">
<title>Brook Lane Sweets – Product Sticker</title>
<link rel="stylesheet" href="https://fonts.googleapis.com/css2?family=Lato:wght@300;400;700;900&display=swap">
<style>
  :root {
    --page-bg: #ece7e1;
    --paper: #ffffff;
    --cocoa-light: #8c4012;
    --cocoa-dark: #4a1f07;
    --cocoa-ink: #3d1e0e;
    --tear-edge: #4cc4d8;
    --accent-orange: #d0661c;
    --accent-blue: #2a86c3;
    --copy-grey: #6b625c;
    --copy-light: #f3e9e1;
  }
  * { margin: 0; padding: 0; box-sizing: border-box; }
  html, body {
    width: 1200px;
    height: 749px;
    overflow: hidden;
    background: var(--page-bg);
    font-family: "Lato", Arial, sans-serif;
  }
  .sticker {
    position: absolute;
    left: 140px;
    top: 45px;
    width: 920px;
    height: 660px;
    overflow: hidden;
    box-shadow: 0 6px 24px rgba(60, 30, 10, 0.18);
  }
  .sticker-surface {
    position: absolute;
    inset: 0;
    width: 100%;
    height: 100%;
  }
  .brand-name {
    position: absolute;
    left: 60px;
    top: 150px;
    width: 360px;
    text-align: center;
    color: var(--cocoa-ink);
    font-weight: 900;
    text-transform: uppercase;
    line-height: 1;
  }
  .brand-name .line-large { display: block; font-size: 78px; letter-spacing: 3px; }
  .brand-name .line-small { display: block; font-size: 34px; letter-spacing: 4px; margin: 10px 0; }
  .tagline {
    position: absolute;
    left: 60px;
    top: 400px;
    width: 380px;
    text-align: center;
    font-size: 27px;
    font-weight: 300;
    color: var(--copy-grey);
    transform: rotate(-4deg);
  }
  .tagline .highlight { color: var(--accent-blue); }
  .feature-list {
    position: absolute;
    right: 40px;
    top: 22px;
    list-style: none;
    text-align: right;
  }
  .feature-list li {
    font-size: 33px;
    font-weight: 300;
    color: var(--accent-orange);
    line-height: 1.3;
  }
  .feature-list li::after {
    content: "";
    display: inline-block;
    width: 9px;
    height: 9px;
    margin-left: 16px;
    border-radius: 50%;
    background: var(--copy-light);
    vertical-align: middle;
  }
  .feature-list li:nth-child(2) { margin-right: 24px; }
  .feature-list li:nth-child(3) { margin-right: 30px; }
  .feature-list li:nth-child(4) { margin-right: 10px; }
  .contact-block {
    position: absolute;
    right: 80px;
    top: 445px;
    text-align: right;
    font-size: 22px;
    font-weight: 300;
    line-height: 1.35;
    color: var(--copy-light);
  }
  .contact-block .website {
    color: var(--accent-orange);
    font-weight: 400;
  }
</style>
</head>
<body>
  <main class="sticker">
    <svg class="sticker-surface" viewBox="0 0 920 660" aria-hidden="true">
      <defs>
        <linearGradient id="cocoa-gradient" x1="0" y1="1" x2="1" y2="0">
          <stop offset="0" stop-color="var(--cocoa-light)"/>
          <stop offset="1" stop-color="var(--cocoa-dark)"/>
        </linearGradient>
      </defs>
      <rect class="cocoa-panel" width="920" height="660" fill="url(#cocoa-gradient)"/>
      <path class="paper-panel"
        d="M0 0 H452 L446 30 L470 48 L458 80 L482 104 L466 132 L492 150 L474 186 L500 206 L486 236 L514 252 L498 290 L526 312 L510 340 L538 360 L522 398 L550 420 L536 450 L562 468 L548 506 L574 528 L560 556 L584 578 L572 612 L590 632 L582 660 H0 Z"
        fill="var(--paper)"/>
      <path class="tear-line" fill="none" stroke="var(--tear-edge)" stroke-width="2.5"
        d="M452 0 L446 30 L470 48 L458 80 L482 104 L466 132 L492 150 L474 186 L500 206 L486 236 L514 252 L498 290 L526 312 L510 340 L538 360 L522 398 L550 420 L536 450 L562 468 L548 506 L574 528 L560 556 L584 578 L572 612 L590 632 L582 660"/>
    </svg>

    <h1 class="brand-name">
      <span class="line-large">Brook</span>
      <span class="line-small">Lane</span>
      <span class="line-large">Sweets</span>
    </h1>

    <p class="tagline"><span class="highlight">Locally</span> Made in <span class="highlight">Austin</span> Texas</p>

    <ul class="feature-list">
      <li>Natural</li>
      <li>Organic</li>
      <li>Vegan</li>
      <li>Gluten free</li>
    </ul>

    <address class="contact-block">
      417 West Harlow Pine Rd<br>
      238 Austin Tx 78719<br>
      <span class="website">www.brooklanesweetsqvz.com</span>
    </address>
  </main>
</body>
</html>
```